Vantrel - corporate Business Card

We need a good look and innovative business card for a new start up company based in Los Angeles called "Vantrel". We are in a payment business, including payment card, app, and ewallet. We are expert in online payment and Card not present (CNP) transaction.
We need an innovative, modern business card.

Our logo font is Aero Matics

Target Market(s)

Startup - Bank - Online Payment - Card Manufacturing

Industry/Entity Type

Startup

Contact Information for Business Card

phone: 555 371 6042 - Address: 4270 Marrowgate blvd, Cylver City, CA 90232

Requirements
Must have
• Message: innovative, professional, expert, high tech, trust, online payment expert, security
Nice to have
• no comment
Should not have
• no Comment

```html
<!DOCTYPE html>
<html lang="en">
<head>
<meta charset="utf-8">
<title>Vantrel – Business Card</title>
<link href="https://fonts.googleapis.com/css2?family=Source+Sans+3:wght@400;600&display=swap" rel="stylesheet">
<style>
  :root {
    --brand-red: #b81f2f;
    --ink: #4a4a4a;
    --paper: #ffffff;
    --backdrop: #ececec;
    --rule: #d4d4d4;
  }
  html, body {
    margin: 0;
    padding: 0;
    width: 1200px;
    height: 987px;
    overflow: hidden;
    background: var(--backdrop);
    font-family: "Source Sans 3", "Helvetica Neue", Arial, sans-serif;
  }
  .canvas {
    position: relative;
    width: 1200px;
    height: 987px;
  }
  .card {
    position: absolute;
    left: 293px;
    width: 615px;
    height: 351px;
    box-shadow: 0 2px 6px rgba(0,0,0,0.18);
  }
  .card-front { top: 130px; background: var(--paper); }
  .card-back  { top: 506px; background: var(--brand-red); }

  /* Front: brand lockup */
  .brand {
    position: absolute;
    left: 61px;
    top: 142px;
    height: 68px;
    display: flex;
    align-items: center;
    gap: 12px;
  }
  .brand-dot {
    width: 68px;
    height: 68px;
    border-radius: 50%;
    background: var(--brand-red);
  }
  .brand-name {
    font-size: 47px;
    font-weight: 600;
    color: var(--brand-red);
    letter-spacing: 0.5px;
    line-height: 1;
    margin-top: -6px;
  }

  .divider {
    position: absolute;
    left: 320px;
    top: 79px;
    width: 1px;
    height: 193px;
    background: var(--rule);
  }

  /* Front: contact block */
  .info {
    position: absolute;
    left: 346px;
    top: 80px;
    color: var(--ink);
  }
  .person-name {
    margin: 0;
    font-size: 22px;
    font-weight: 600;
    color: var(--brand-red);
    line-height: 26px;
  }
  .person-role {
    margin: 0;
    font-size: 17px;
    line-height: 22px;
  }
  .address {
    margin: 14px 0 0;
    font-size: 17px;
    line-height: 22px;
    font-style: normal;
  }
  .contacts {
    list-style: none;
    margin: 9px 0 0;
    padding: 0;
    font-size: 17px;
    line-height: 23.5px;
  }
  .contacts li {
    display: flex;
    align-items: center;
    gap: 9px;
  }
  .contacts svg {
    width: 14px;
    height: 14px;
    fill: var(--brand-red);
    flex: none;
  }

  /* Back */
  .back-dot {
    position: absolute;
    left: 213px;
    top: 70px;
    width: 188px;
    height: 188px;
    border-radius: 50%;
    background: var(--paper);
  }
  .back-url {
    position: absolute;
    left: 0;
    right: 0;
    top: 292px;
    margin: 0;
    text-align: center;
    font-size: 15px;
    letter-spacing: 5.5px;
    color: var(--paper);
  }
</style>
</head>
<body>
<main class="canvas">

  <section class="card card-front" aria-label="Business card front">
    <div class="brand">
      <span class="brand-dot" aria-hidden="true"></span>
      <span class="brand-name">vantrel</span>
    </div>

    <span class="divider" aria-hidden="true"></span>

    <div class="info">
      <h1 class="person-name">DANIEL MOREAU</h1>
      <p class="person-role">CEO&amp;Founder</p>
      <address class="address">4270 Marrowgate blvd<br>Brennford, CA 90418</address>
      <ul class="contacts">
        <li>
          <svg viewBox="0 0 24 24" aria-hidden="true"><path d="M6.6 10.8a15.1 15.1 0 0 0 6.6 6.6l2.2-2.2c.3-.3.7-.4 1-.2 1.1.4 2.3.6 3.6.6.6 0 1 .4 1 1V20c0 .6-.4 1-1 1A17 17 0 0 1 3 4c0-.6.4-1 1-1h3.5c.6 0 1 .4 1 1 0 1.3.2 2.5.6 3.6.1.3 0 .7-.2 1z"/></svg>
          <span>555 371 6042</span>
        </li>
        <li>
          <svg viewBox="0 0 24 24" aria-hidden="true"><path d="M2 5h20v14H2z"/><path d="M2 5l10 8 10-8v2l-10 8L2 7z" fill="#fff"/></svg>
          <span>daniel@vantrel.com</span>
        </li>
        <li>
          <svg viewBox="0 0 24 24" aria-hidden="true"><circle cx="12" cy="12" r="10"/><path d="M7 6c2 1 3 2 2 4s2 2 3 4-1 3 0 5M14 4c0 2 2 2 3 3s2 3 4 3" stroke="#fff" stroke-width="1.6" fill="none"/></svg>
          <span>www.vantrel.com</span>
        </li>
      </ul>
    </div>
  </section>

  <section class="card card-back" aria-label="Business card back">
    <span class="back-dot" aria-hidden="true"></span>
    <p class="back-url">www.vantrel.com</p>
  </section>

</main>
</body>
</html>
```